Healer at the Hearth needs business card

We need a business card that reflects the look and feel of the new website at www.healerathehearth.ca

Our patient navigation and advocacy services are most commonly used by seniors who feel overwhelmed by the health care system and want someone on their side to advocate for their care. Individuals with ill parents or other family members may also come to rely on Healer at the Hearth to help them support their loved one through their health care journey. Ultimately, anyone who finds their health care experience challenging and wants someone completely focused on their needs can benefit from the services of our doctor / nurse team.

Business

Must have
• One design tailored for two clinician which should include: logo, name, title, tel, email, web address and tagline
Nice to have
• A banner image to create a similar look to the website at www.healerathehearth.ca
Should not have
• Too cluttered or busy - must be clean and professional

```html
<!DOCTYPE html>
<html lang="en">
<head>
<meta charset="utf-8">
<title>Healer at the Hearth – business cards</title>
<link rel="stylesheet" href="https://fonts.googleapis.com/css2?family=Jost:wght@400;500&family=EB+Garamond:ital,wght@1,400&display=swap">
<style>
  :root {
    --page: #ffffff;
    --ink: #1a1a1a;
    --red: #a01c24;
    --blue: #2f6490;
    --blue-card: #336590;
    --cream: #e8e4d8;
    --paper: #f2f1ec;
    --band: #ebe8dc;
    --soft: #f3f2ee;
    --web-band: #e0e0e6;
    --edge: #a9a9a9;
  }
  * { box-sizing: border-box; margin: 0; padding: 0; }
  html, body { width: 1200px; height: 927px; overflow: hidden; background: var(--page); }
  body { position: relative; font-family: "Jost", sans-serif; color: var(--ink); }

  .sheet-title {
    position: absolute; left: 35px; top: 28px;
    font-size: 28px; font-weight: 400; letter-spacing: -0.2px;
  }

  .card {
    position: absolute; top: 253px; width: 218px; height: 382px;
    border: 1px solid var(--edge); overflow: hidden;
  }
  .card--cream { left: 110px; background: var(--cream); }
  .card--blue { left: 350px; background: var(--blue-card); border-color: var(--blue-card); }
  .card--paper { left: 625px; background: var(--paper); }
  .card--banded { left: 876px; background: var(--page); }

  .line { position: absolute; left: 0; right: 0; text-align: center; white-space: nowrap; }

  /* front-side mark */
  .front-mark { position: absolute; left: 0; right: 0; top: 100px; text-align: center; }
  .front-mark__dot { width: 70px; height: 70px; border-radius: 50%; margin: 0 auto 14px; }
  .front-mark__name { font-size: 17px; font-weight: 500; line-height: 1.2; }
  .card--cream .front-mark__dot { background: var(--red); }
  .card--cream .front-mark__name { color: var(--red); }
  .card--blue .front-mark__dot { background: #ffffff; }
  .card--blue .front-mark__name { color: #ffffff; }

  .tagline--serif {
    font-family: "EB Garamond", serif; font-style: italic;
    font-size: 17px; line-height: 26px; color: var(--blue); top: 306px;
  }
  .tagline--sans {
    font-size: 16px; line-height: 22px; color: #ffffff; top: 314px;
  }

  /* back-side brand */
  .brand { position: absolute; left: 22px; top: 28px; display: flex; align-items: center; gap: 8px; }
  .brand__dot { width: 40px; height: 40px; border-radius: 50%; background: var(--red); flex: none; }
  .brand__name { font-size: 21px; line-height: 24px; color: var(--blue); font-weight: 400; }
  .card--banded .brand { top: 30px; }

  .person-name { font-size: 25px; font-weight: 400; line-height: 30px; }
  .person-title { font-size: 12px; font-weight: 500; line-height: 16px; }
  .label { font-size: 10px; font-weight: 500; line-height: 12px; }
  .value { font-size: 16px; line-height: 20px; }
  .web { font-size: 15px; font-weight: 500; line-height: 20px; }

  .card--paper .person-name { top: 155px; }
  .card--paper .person-title { top: 190px; }
  .card--paper .label--tel { top: 248px; }
  .card--paper .value--tel { top: 263px; }
  .card--paper .label--mail { top: 296px; }
  .card--paper .value--mail { top: 311px; }
  .card--paper .web { top: 349px; }

  .band { position: absolute; left: 0; right: 0; }
  .band--name { top: 137px; height: 74px; background: var(--band); }
  .band--contact { top: 218px; height: 116px; background: var(--soft); }
  .band--web { top: 339px; height: 43px; background: var(--web-band); }
  .card--banded .line--right { text-align: right; right: 11px; left: auto; }
  .card--banded .person-name { top: 18px; }
  .card--banded .person-title { top: 45px; }
  .card--banded .label--tel { top: 18px; }
  .card--banded .value--tel { top: 32px; }
  .card--banded .label--mail { top: 66px; }
  .card--banded .value--mail { top: 80px; right: auto; left: 0; width: 100%; text-align: center; }
  .card--banded .web { top: 11px; }
</style>
</head>
<body>
  <h1 class="sheet-title">Healer at the Hearth - business card landscape designs</h1>

  <section class="card card--cream" aria-label="Card front, cream">
    <div class="front-mark">
      <div class="front-mark__dot"></div>
      <p class="front-mark__name">Healer at the Hearth</p>
    </div>
    <p class="line tagline--serif">Patient Navigation<br>&amp; Advocacy Services</p>
  </section>

  <section class="card card--blue" aria-label="Card front, blue">
    <div class="front-mark">
      <div class="front-mark__dot"></div>
      <p class="front-mark__name">Healer at the Hearth</p>
    </div>
    <p class="line tagline--sans">Patient Navigation<br>&amp; Advocacy Services</p>
  </section>

  <section class="card card--paper" aria-label="Card back, plain">
    <div class="brand">
      <span class="brand__dot"></span>
      <span class="brand__name">Healer at<br>the Hearth</span>
    </div>
    <p class="line person-name">Martin Ashford</p>
    <p class="line person-title">MD &amp; Co-Founder</p>
    <p class="line label label--tel">Telephone:</p>
    <p class="line value value--tel">647-555-0142</p>
    <p class="line label label--mail">Email:</p>
    <p class="line value value--mail">info@healerathehearth.ca</p>
    <p class="line web">www.healerathehearth.ca</p>
  </section>

  <section class="card card--banded" aria-label="Card back, banded">
    <div class="brand">
      <span class="brand__dot"></span>
      <span class="brand__name">Healer at<br>the Hearth</span>
    </div>
    <div class="band band--name">
      <p class="line line--right person-name">Martin Ashford</p>
      <p class="line line--right person-title">MD &amp; Co-Founder</p>
    </div>
    <div class="band band--contact">
      <p class="line line--right label label--tel">Telephone:</p>
      <p class="line line--right value value--tel">647-555-0142</p>
      <p class="line line--right label label--mail">Email:</p>
      <p class="line value value--mail">info@healerathehearth.ca</p>
    </div>
    <div class="band band--web">
      <p class="line web">www.healerathehearth.ca</p>
    </div>
  </section>
</body>
</html>
```